Orvalline Consulting Group Business Card Design

We have the logo we just need someone to design a modern business card design.

Name: Leopold Ganzhurt
Phone: 3052918364
Mobile: 9178402297
Web:www.orvallineconsulting.com
email: lganzhurt@orvallineconsulting.com
Company: Orvalline Consulting Group
Title: CEO

Address: 718 Quenby Ave, Miami, Florida 33187

Target Market(s)

companies over 100 employees

Industry/Entity Type

Business

```html
<!DOCTYPE html>
<html lang="en">
<head>
<meta charset="utf-8">
<title>Orvalline Consulting Group – Business Card</title>
<link rel="stylesheet" href="https://fonts.googleapis.com/css2?family=Archivo:wght@800&family=Arimo:wght@400;700&display=swap">
<style>
  :root{
    --backdrop:#c6c7c9;
    --card:#ffffff;
    --brand-blue:#3c5fab;
    --ink:#111111;
    --text-grey:#4a4a4a;
    --rule:#b5b5b5;
    --band-dark:#0b0b0d;
  }
  *{margin:0;padding:0;box-sizing:border-box}
  html,body{width:1200px;height:720px;overflow:hidden;background:var(--backdrop)}
  .stage{position:relative;width:1200px;height:720px;font-family:"Arimo",Arial,sans-serif}
  .card{position:absolute;top:237px;width:486px;height:280px;background:var(--card);border-radius:18px;overflow:hidden}
  .card--front{left:80px}
  .card--back{left:629px}

  .mark{position:absolute;border-radius:50%;background:var(--brand-blue)}
  .wordmark{position:absolute;text-align:center;font-family:"Archivo",Arial,sans-serif;font-weight:800;color:var(--ink);line-height:1}
  .wordmark__name{display:block;font-size:25px;letter-spacing:0.6px}
  .wordmark__sub{display:block;font-size:9.5px;letter-spacing:0.5px;margin-top:3px}

  .card--front .mark{left:334px;top:19px;width:76px;height:76px}
  .card--front .wordmark{left:252px;top:107px;width:240px}

  .person{position:absolute;left:19px;top:162px}
  .person__name{font-size:15px;color:var(--brand-blue);line-height:1}
  .person__title{font-size:11px;color:var(--ink);margin-top:3px;line-height:1}
  .divider{position:absolute;left:19px;top:202px;width:451px;height:1px;background:var(--rule)}

  .contact{position:absolute;top:220px;font-size:11px;color:var(--text-grey);line-height:16px}
  .contact--address{left:19px;top:223px;line-height:15px}
  .contact--phones{left:158px}
  .contact--online{left:268px}
  .contact__row{display:flex;align-items:center;gap:7px;white-space:nowrap}
  .contact__row svg{width:12px;height:12px;flex:none;fill:var(--brand-blue)}

  .card--back .mark{left:197px;top:66px;width:62px;height:62px}
  .card--back .wordmark{left:108px;top:139px;width:240px}
  .card--back .wordmark__name{font-size:20px}
  .card--back .wordmark__sub{font-size:8.5px}

  .web-band{position:absolute;left:0;top:215px;width:486px;height:40px;
    background:linear-gradient(90deg,var(--brand-blue) 0%,var(--brand-blue) 62%,#1e2d52 80%,var(--band-dark) 100%)}
  .web-band__url{position:absolute;left:0;width:445px;top:0;line-height:40px;text-align:center;
    color:#fff;font-weight:700;font-size:11.5px}
  .band-mark{position:absolute;left:351px;top:187px;width:88px;height:88px;border-radius:50%;background:var(--card)}
  .band-mark .mark{left:7px;top:7px;width:74px;height:74px}
</style>
</head>
<body>
<main class="stage">

  <section class="card card--front" aria-label="Card front">
    <span class="mark" aria-hidden="true"></span>
    <p class="wordmark"><span class="wordmark__name">ORVALLINE</span><span class="wordmark__sub">CONSULTING GROUP</span></p>

    <div class="person">
      <p class="person__name">Leopold Ganzhurt</p>
      <p class="person__title">CEO</p>
    </div>
    <div class="divider"></div>

    <div class="contact contact--address">
      <p>718 Quenby Ave</p>
      <p>Miami, Florida 33187</p>
    </div>

    <div class="contact contact--phones">
      <p class="contact__row">
        <svg viewBox="0 0 12 12" aria-hidden="true"><path d="M1 4.5C1 2.5 3 1.5 6 1.5s5 1 5 3v1H8.6V4.2H3.4v1.3H1z"/><rect x="2.5" y="6" width="7" height="5" rx="1"/></svg>
        3052918364
      </p>
      <p class="contact__row">
        <svg viewBox="0 0 12 12" aria-hidden="true"><path d="M3.5 0.5h5a1 1 0 0 1 1 1v9a1 1 0 0 1-1 1h-5a1 1 0 0 1-1-1v-9a1 1 0 0 1 1-1zm0.4 1.4v7.4h4.2V1.9z"/></svg>
        9178402297
      </p>
    </div>

    <div class="contact contact--online">
      <p class="contact__row">
        <svg viewBox="0 0 12 12" aria-hidden="true"><path d="M1 2h10v6.5H1zm1.2 1.2v4.1h7.6V3.2zM4.5 9.3h3v1H4.5z"/></svg>
        www.orvallineconsulting.com
      </p>
      <p class="contact__row">
        <svg viewBox="0 0 12 12" aria-hidden="true"><path d="M1 2.5h10v7H1zm1 1v.3L6 6.5l4-2.7v-.3zm0 1.6V8.5h8V5.1L6 7.8z"/></svg>
        lganzhurt@orvallineconsulting.com
      </p>
    </div>
  </section>

  <section class="card card--back" aria-label="Card back">
    <span class="mark" aria-hidden="true"></span>
    <p class="wordmark"><span class="wordmark__name">ORVALLINE</span><span class="wordmark__sub">CONSULTING GROUP</span></p>

    <div class="web-band">
      <p class="web-band__url">www.orvallineconsulting.com</p>
    </div>
    <div class="band-mark" aria-hidden="true"><span class="mark"></span></div>
  </section>

</main>
</body>
</html>
```